Rise To Go Further! - Marketing, Training, Managment for Multifamily Professionals

Flyer for training event. I have to be able to edit location, times, speakers, cost,
We will have 2 to 4 speakers for each event. Each event may have a different topic relating to the main topic (Marketing, Training, Management). The idea is to get as many people to open or pick up the fly and say "I have to attend" this seminar. We are the experts in the industry and want to portray this with the flyer. Each speaker will have a topic and a certain amount of time. Each topic will be different.
Updates

Project Deadline Extended
Reason: I apologize for the new design deadline. I've been traveling extensively for work and unable to view submissions. Currently I am not traveling and able to dedicate time to view all of the wonderful submissions. I'm looking forward to selecting one. Thank you all for your understanding.

Target Market(s)

Multifamily - Apartment Communities, Owners, Apartment Associations, Leasing Agents, Marketing Directors, Managers, Presidents,

Industry/Entity Type

Marketing

Colors

Designer to choose colors to be used in the design.

Requirements
Must have
• Editable flyer. I have to be able to edit; location, times/date, speaker, cost, description.
• Sponsored by Tovali Power attached Logo for TVP
Nice to have
• Spot for photo of each speaker (2-4) speaker

```html
<!DOCTYPE html>
<html lang="en">
<head>
<meta charset="utf-8">
<title>Marketing Training 2017 – Event Flyer</title>
<link href="https://fonts.googleapis.com/css2?family=Bebas+Neue&family=Open+Sans:wght@400;700&display=swap" rel="stylesheet">
<style>
  :root {
    --brand-blue: #00aeef;
    --accent-blue: #1a94d4;
    --brand-green: #39b54a;
    --bar-green: #7dc242;
    --ink: #3a3a3a;
    --body-ink: #444444;
    --paper: #ffffff;
    --photo-dark: #4a3a36;
    --photo-warm: #b58a78;
    --backdrop: #808080;
  }
  * { margin: 0; padding: 0; box-sizing: border-box; }
  html, body { width: 923px; height: 1200px; overflow: hidden; background: var(--backdrop); }
  .flyer {
    position: relative; width: 923px; height: 1200px; background: var(--paper);
    font-family: "Open Sans", sans-serif; overflow: hidden;
  }
  .flyer-art { position: absolute; inset: 0; }
  .brand-tab {
    position: absolute; left: 73px; top: 0; width: 208px; height: 150px;
    background: var(--paper); border-radius: 0 0 20px 20px;
    display: flex; align-items: center; justify-content: center; gap: 10px;
  }
  .brand-name { font-family: "Open Sans", sans-serif; font-weight: 700; font-size: 50px; color: #1b1b1b; letter-spacing: -1px; }
  .brand-dot { width: 14px; height: 14px; background: var(--brand-blue); }
  .event-title {
    position: absolute; left: 255px; top: 412px; width: 410px; text-align: center;
    font-family: "Bebas Neue", sans-serif; color: var(--paper);
    font-size: 92px; line-height: 79px;
  }
  .event-description {
    position: absolute; left: 116px; top: 712px; width: 692px; text-align: center;
    font-size: 17px; line-height: 21.5px; color: var(--body-ink);
  }
  .speaker { position: absolute; top: 836px; width: 200px; text-align: center; }
  .speaker-name {
    margin-top: 14px; font-weight: 700; font-size: 17px; color: var(--accent-blue);
    text-transform: uppercase;
  }
  .event-details {
    position: absolute; top: 1090px; font-weight: 700; font-size: 22px; line-height: 30px;
    color: var(--ink); text-transform: uppercase;
  }
  .event-when { right: 497px; text-align: right; }
  .event-where { left: 497px; text-align: left; }
</style>
</head>
<body>
<main class="flyer">
  <svg class="flyer-art" width="923" height="1200" viewBox="0 0 923 1200">
    <defs>
      <linearGradient id="photoTone" x1="0" y1="0" x2="1" y2="1">
        <stop offset="0" stop-color="#5a4640"/>
        <stop offset="0.5" stop-color="var(--photo-warm)"/>
        <stop offset="1" stop-color="#2e3a4a"/>
      </linearGradient>
      <linearGradient id="headshotTone" x1="0" y1="0" x2="0" y2="1">
        <stop offset="0" stop-color="#f2f2f2"/>
        <stop offset="1" stop-color="#c9cfd6"/>
      </linearGradient>
    </defs>
    <rect class="hero-photo" role="img" aria-label="Photo: speaker presenting on stage to a large conference audience" x="0" y="0" width="923" height="620" fill="url(#photoTone)"/>
    <path class="wave-blue" d="M540 620 C700 470 850 380 923 234 L923 330 C820 440 700 520 600 620 Z" fill="var(--brand-blue)"/>
    <path class="wave-green" d="M0 392 C250 560 650 520 923 345 L923 370 C650 560 250 600 0 540 Z" fill="var(--brand-green)"/>
    <path class="wave-rule" d="M0 392 C250 560 650 520 923 345" fill="none" stroke="var(--paper)" stroke-width="6"/>
    <path class="page-body" d="M0 540 C250 600 650 560 923 370 L923 1200 L0 1200 Z" fill="var(--paper)"/>
    <circle class="title-ring" cx="460" cy="497" r="222" fill="var(--paper)"/>
    <circle class="title-badge" cx="460" cy="497" r="208" fill="var(--brand-blue)"/>

    <g class="speaker-photos">
      <circle role="img" aria-label="Speaker photo: Daniel Shaw" cx="252" cy="919" r="80" fill="url(#headshotTone)" stroke="var(--accent-blue)" stroke-width="4"/>
      <circle role="img" aria-label="Speaker photo: Amelia Jordan" cx="463" cy="919" r="80" fill="url(#headshotTone)" stroke="var(--accent-blue)" stroke-width="4"/>
      <circle role="img" aria-label="Speaker photo: Jonah Mills" cx="674" cy="919" r="80" fill="url(#headshotTone)" stroke="var(--accent-blue)" stroke-width="4"/>
    </g>

    <line class="details-rule" x1="130" y1="1058" x2="793" y2="1058" stroke="var(--accent-blue)" stroke-width="3"/>
    <line class="details-divider" x1="463" y1="1080" x2="463" y2="1160" stroke="var(--accent-blue)" stroke-width="3"/>

    <rect class="footer-bar-blue" x="0" y="1177" width="714" height="23" fill="var(--brand-blue)"/>
    <rect class="footer-bar-green" x="722" y="1177" width="201" height="23" fill="var(--bar-green)"/>
  </svg>

  <div class="brand-tab">
    <span class="brand-name">TVP</span>
    <span class="brand-dot"></span>
  </div>

  <h1 class="event-title">Marketing<br>Training<br>2017</h1>

  <p class="event-description">Lorem ipsum dolor sit amet, consectetur adipiscing elit. Nunc tellus augue, luctus sit amet fringilla et, elementum sit amet nulla. Vivamus at eros euismod, ultricies velit eu, tempor ipsum. Duis vehicula pretium nisi a mollis. Nullam ligula ligula, egestas vel malesuada id, faucibus at tortor. In hac habitasse</p>

  <div class="speaker" style="left:152px; top:1008px;"><p class="speaker-name">Daniel Shaw</p></div>
  <div class="speaker" style="left:363px; top:1008px;"><p class="speaker-name">Amelia Jordan</p></div>
  <div class="speaker" style="left:574px; top:1008px;"><p class="speaker-name">Jonah Mills</p></div>

  <div class="event-details event-when">20 October 2017<br>10AM - 12PM</div>
  <div class="event-details event-where">Harbor View Hotel<br>San Francisco</div>
</main>
</body>
</html>
```